continuing medical education travel company. luxury, professional, quality service

PLEASE USE THE REVISED LOGO FOR ALL CARD DESIGNS, NO SNAKE HEAD

Target Market(s)

physicians

Industry/Entity Type

Travel Industry

Contact Information for Business Card

luxury quality, spot uv, foil, rounded corners

Colors
0255a3
3176b5
cfdeed
aaaaaa
5c5c5c

Requirements
Must have
• navy, platinum, possible holographic

```html
<!DOCTYPE html>
<html lang="en">
<head>
<meta charset="utf-8">
<title>Halden Travel – Business Cards</title>
<link rel="stylesheet" href="https://fonts.googleapis.com/css2?family=Roboto:wght@400;500&display=swap">
<style>
  :root {
    --navy: #0255a3;
    --mid-blue: #3176b5;
    --ice: #cfdeed;
    --platinum: #aaaaaa;
    --graphite: #5c5c5c;
    --white: #ffffff;
    --backdrop: #eceff3;
  }
  * { box-sizing: border-box; margin: 0; padding: 0; }
  html, body { width: 1200px; height: 902px; overflow: hidden; }
  body {
    background: var(--backdrop);
    font-family: "Roboto", Arial, sans-serif;
    position: relative;
  }
  .card {
    position: absolute;
    top: 296px;
    width: 540px;
    height: 310px;
    border-radius: 18px;
    background: var(--navy);
    overflow: hidden;
    box-shadow: 0 10px 24px rgba(0,0,0,0.18);
    color: var(--white);
  }
  .card--front { left: 40px; }
  .card--back { left: 620px; }

  .band {
    position: absolute;
    left: 0; right: 0; bottom: 0;
    height: 38px;
    background: linear-gradient(90deg, var(--platinum), #c4c4c4 50%, var(--platinum));
    display: flex;
    align-items: center;
    padding: 0 26px;
    font-size: 14px;
    letter-spacing: 1px;
    color: var(--white);
  }
  .band svg { width: 12px; height: 14px; margin-right: 8px; fill: var(--white); }

  .corner-mark {
    position: absolute;
    right: 20px;
    bottom: 46px;
    font-size: 13px;
    font-weight: 500;
    letter-spacing: 1px;
    color: var(--ice);
  }

  .identity {
    position: absolute;
    left: 40px;
    top: 92px;
    text-align: right;
    width: 250px;
  }
  .identity__name {
    font-size: 26px;
    letter-spacing: 0.5px;
    white-space: nowrap;
  }
  .identity__title {
    display: inline-block;
    margin-top: 10px;
    background: var(--mid-blue);
    padding: 6px 18px;
    font-size: 16px;
    letter-spacing: 1px;
    color: var(--ice);
  }
  .divider {
    position: absolute;
    left: 306px;
    top: 80px;
    width: 2px;
    height: 90px;
    background: var(--ice);
  }
  .contacts {
    position: absolute;
    left: 322px;
    top: 82px;
    list-style: none;
    font-size: 12.5px;
    line-height: 30px;
    color: var(--ice);
  }
  .contacts li { display: flex; align-items: center; }
  .contacts svg { width: 14px; height: 14px; margin-right: 8px; fill: var(--ice); }

  .brand-lockup {
    position: absolute;
    left: 0; right: 0;
    top: 108px;
    display: flex;
    justify-content: center;
    align-items: center;
    gap: 14px;
  }
  .brand-lockup__dot {
    width: 18px; height: 18px;
    border-radius: 50%;
    background: var(--ice);
  }
  .brand-lockup__name {
    font-size: 34px;
    letter-spacing: 6px;
    color: var(--ice);
  }
</style>
</head>
<body>

<section class="card card--front" aria-label="Business card front">
  <div class="identity">
    <div class="identity__name">LAURA BENTON</div>
    <div class="identity__title">PRINCIPAL</div>
  </div>
  <div class="divider"></div>
  <ul class="contacts">
    <li><svg viewBox="0 0 14 14"><rect x="3" y="0.5" width="8" height="13" rx="1.5"/></svg>514.555.0187</li>
    <li><svg viewBox="0 0 14 14"><path d="M1 3h12v8H1z M1 3l6 5 6-5" fill="none" stroke="#cfdeed" stroke-width="1.4"/></svg>lbenton@haldentravel.com</li>
    <li><svg viewBox="0 0 14 14"><circle cx="7" cy="7" r="6" fill="none" stroke="#cfdeed" stroke-width="1.4"/><path d="M1 7h12M7 1c-3 3-3 9 0 12M7 1c3 3 3 9 0 12" fill="none" stroke="#cfdeed" stroke-width="1"/></svg>www.haldentravel.com</li>
  </ul>
  <div class="corner-mark">HALDEN TRAVEL</div>
  <div class="band">
    <svg viewBox="0 0 12 14"><path d="M6 0a5 5 0 0 1 5 5c0 4-5 9-5 9S1 9 1 5a5 5 0 0 1 5-5zm0 3a2 2 0 1 0 0 4 2 2 0 0 0 0-4z"/></svg>
    48 Maple Ave. Lakeview, QC H1A 2B3
  </div>
</section>

<section class="card card--back" aria-label="Business card back">
  <div class="brand-lockup">
    <span class="brand-lockup__dot"></span>
    <span class="brand-lockup__name">HALDEN TRAVEL</span>
  </div>
  <div class="corner-mark">HALDEN TRAVEL</div>
  <div class="band">HALDEN TRAVEL</div>
</section>

</body>
</html>
```